Rapidly-Growing OTA Needs Catchy Banners in HTML5!

We need simple catchy banners in HTML5!

Airvento is a global startup, an online travel agent selling flights. Our technology allows us to combine low-cost and traditional carriers and thus create unique routes not offered by any other OTA. And often up to 90% cheaper!

We want you to create an elegant banner with simple, not overly intrusive, animation, that calls for action.

Goals for the banner - click-through action and building brand awareness.

7 Sizes:

300x250
336x280
728x90
480x60
120x600
160x600
300x600

Provide the animated version in HTML5 + standard picture for each size.

Please, keep the file size of animated .zip down to max 150 kB and picture size to 40kB!

Can contain slides. (e.g. Attention-catching text => animation => logo with call-to-action etc).

Logo (in various sizes) attached.
Font used in for Airvento name - Gotham Rounded.
Use Sans Serif.

Text variations attached - you can edit it, add more, if you come up with a better one - plus points :-) But don't digress from the idea of cheap flights. And keep it simple.

Choose the animations as you wish, but simple and professional (venny, the bird maskot, can "fly", clouds can move.. it's up to you).

Creativity and catchiness is the most important aspect!

Logo (venny) with our name, short slogan and a strong call-to-action is a must. The design should evoke flying - up to you how (clouds, sky, shades of blue, etc.)

Our website is newly redesigned in material design and banners should correspond with colors used. www.airvento-example.com

Possible long-term cooperation, if the job is well done!

Target Market(s)

Travel segment, portals, blogs, travellers

Industry/Entity Type

Travel Industry

Font styles to use
Sans Serif

Requirements
Must have
• Logo
• Slogan
• Call-to-action
• Elegant animation
• Correspond with brand (www.airvento-example.com)
Should not have
• Intrusive animations
• Too long messages

```html
<!DOCTYPE html>
<html lang="en">
<head>
<meta charset="utf-8">
<title>Airvento – Find the cheapest flights</title>
<link href="https://fonts.googleapis.com/css2?family=Open+Sans:wght@600;700;800&display=swap" rel="stylesheet">
<style>
  :root {
    --sky-top: #0b2546;
    --sky-mid: #1f5d9c;
    --sky-low: #5b93c8;
    --cloud-light: #e6edf3;
    --cloud-soft: #c9d6e2;
    --badge-fill: #2b3e57;
    --badge-ring: rgba(140, 170, 205, 0.55);
    --white: #ffffff;
    --headline-red: #e1251b;
    --headline-dark: #1e1e1e;
    --headline-orange: #f46a16;
    --cta-red: #d9231d;
    --code-grey: #333333;
  }
  html, body {
    margin: 0;
    padding: 0;
    width: 1200px;
    height: 2400px;
    overflow: hidden;
    background: #ffffff;
  }
  .banner {
    position: relative;
    width: 1200px;
    height: 2400px;
    overflow: hidden;
    font-family: "Open Sans", Arial, sans-serif;
  }
  .banner__scene {
    position: absolute;
    inset: 0;
    background:
      radial-gradient(ellipse 700px 260px at 560px 880px, rgba(235, 242, 250, 0.55), rgba(235, 242, 250, 0) 70%),
      linear-gradient(180deg,
        var(--sky-top) 0%,
        var(--sky-mid) 30%,
        var(--sky-low) 48%,
        var(--cloud-soft) 60%,
        var(--cloud-light) 78%,
        #f2f5f8 100%);
  }
  .brand {
    position: absolute;
    top: 210px;
    left: 0;
    width: 100%;
    display: flex;
    justify-content: center;
    align-items: center;
    gap: 28px;
  }
  .brand__dot {
    width: 96px;
    height: 96px;
    border-radius: 50%;
    background: var(--white);
  }
  .brand__name {
    color: var(--white);
    font-weight: 800;
    font-size: 82px;
    letter-spacing: 2px;
    line-height: 1;
  }
  .badge {
    position: absolute;
    left: 580px;
    top: 980px;
    width: 560px;
    height: 560px;
    border-radius: 50%;
    background: var(--badge-fill);
    box-shadow: 0 0 0 26px var(--badge-ring);
    display: flex;
    align-items: center;
    justify-content: center;
    text-align: center;
  }
  .badge__text {
    color: var(--white);
    font-weight: 600;
    font-size: 46px;
    line-height: 1.55;
    letter-spacing: 0.5px;
  }
  .headline {
    position: absolute;
    left: 140px;
    top: 1440px;
    margin: 0;
    font-weight: 800;
    line-height: 1;
    text-transform: uppercase;
  }
  .headline__line { display: block; }
  .headline__line--find {
    color: var(--headline-red);
    font-size: 212px;
    letter-spacing: -2px;
  }
  .headline__line--cheapest {
    color: var(--headline-dark);
    font-size: 110px;
    margin-top: 14px;
  }
  .headline__line--flights {
    color: var(--headline-orange);
    font-size: 200px;
    margin-top: 6px;
    letter-spacing: -2px;
  }
  .cta {
    position: absolute;
    left: 140px;
    top: 2000px;
    width: 608px;
    height: 200px;
    background: var(--cta-red);
    color: var(--white);
    font-weight: 700;
    font-size: 66px;
    display: flex;
    align-items: center;
    justify-content: center;
    text-decoration: none;
    letter-spacing: 1px;
  }
  .ad-code {
    position: absolute;
    right: 64px;
    bottom: 44px;
    color: var(--code-grey);
    font-weight: 600;
    font-size: 50px;
  }
</style>
</head>
<body>
  <div class="banner">
    <div class="banner__scene" role="img" aria-label="Photograph of a white passenger jet flying through a deep blue sky above a layer of white clouds"></div>

    <div class="brand">
      <span class="brand__dot"></span>
      <span class="brand__name">AIRVENTO</span>
    </div>

    <div class="badge">
      <p class="badge__text">UNIQUE FLIGHT<br>COMBINATIONS</p>
    </div>

    <h1 class="headline">
      <span class="headline__line headline__line--find">Find</span>
      <span class="headline__line headline__line--cheapest">The cheapest</span>
      <span class="headline__line headline__line--flights">Flights!</span>
    </h1>

    <a class="cta" href="#">FLY NOW!</a>

    <span class="ad-code">C8</span>
  </div>
</body>
</html>
```